The Bridgewell Counseling Group - Practice Flyer

We need a flyer that generally advertises our services. I've uploaded one old flyer as well as examples of others. I like the style of the materials made by this practice: https://www.facebook.com/MarlowTherapyStudioNorth

```html
<!DOCTYPE html>
<html lang="en">
<head>
<meta charset="utf-8">
<title>The Bridgewell Counseling Group – Practice Flyer</title>
<link rel="stylesheet" href="https://fonts.googleapis.com/css2?family=Cinzel:wght@400;700&family=Merriweather:ital,wght@0,300;0,400;0,700;1,300;1,400&display=swap">
<style>
  :root {
    --forest: #2f4128;
    --forest-deep: #26361f;
    --olive: #9c9b68;
    --sand: #e6e4c8;
    --sand-light: #efeedb;
    --sand-pale: #f4f3e6;
    --ink: #2b2b28;
    --white: #ffffff;
    --photo-warm: #b9a58f;
    --photo-cool: #dfe3e2;
  }
  * { box-sizing: border-box; margin: 0; padding: 0; }
  html, body { width: 1200px; height: 1200px; overflow: hidden; }
  body {
    background: #e9e9e9;
    font-family: "Merriweather", Georgia, serif;
    color: var(--ink);
    position: relative;
  }
  .flyer {
    position: absolute;
    left: 210px; top: 53px;
    width: 780px; height: 1094px;
    background: var(--white);
    overflow: hidden;
  }
  .abs { position: absolute; }

  .hero-photo {
    left: 230px; top: 0; width: 550px; height: 420px;
    background: linear-gradient(90deg, rgba(255,255,255,1) 0%, rgba(255,255,255,0) 22%),
                linear-gradient(180deg, var(--photo-cool) 0%, #c8b6a4 45%, #6a4a3a 80%, #4b3a33 100%);
  }
  .backdrop { left: 0; top: 0; width: 780px; height: 1094px; }

  .title {
    left: 41px; top: 84px;
    font-family: "Cinzel", "Times New Roman", serif;
    color: var(--forest);
  }
  .title-main { font-size: 30px; font-weight: 700; line-height: 34px; letter-spacing: 0.5px; display: block; }
  .title-sub { font-size: 20px; font-weight: 400; line-height: 30px; letter-spacing: 1px; display: block; margin-top: 2px; }
  .title-rule { left: 44px; top: 206px; width: 80px; height: 2px; background: var(--forest); }

  .intro {
    left: 41px; top: 229px; width: 270px;
    font-size: 11.6px; font-weight: 300; line-height: 20.5px;
  }
  .intro strong { font-weight: 700; }

  .circle-photo {
    left: 510px; top: 286px; width: 218px; height: 218px; border-radius: 50%;
    border: 4px solid var(--white);
    background: linear-gradient(135deg, #e7e2d8 0%, #b8a58d 45%, #5d4b3f 100%);
  }

  .lead {
    left: 50px; top: 413px; width: 360px;
    font-size: 11.5px; font-weight: 300; line-height: 19px;
  }
  .conditions {
    list-style: none; font-size: 11.6px; font-weight: 300;
  }
  .conditions li { height: 23px; line-height: 23px; }
  .conditions li::before { content: "▸ "; font-size: 8px; vertical-align: 1px; }
  .conditions-left { left: 52px; top: 474px; }
  .conditions-right { left: 313px; top: 474px; }

  .head-illustration {
    left: 532px; top: 514px; width: 124px; height: 130px;
    border-radius: 50% 50% 30% 40%;
    background: radial-gradient(circle at 55% 40%, #e4a7b4 0%, #d8c779 25%, #a7b26c 45%, rgba(230,228,200,0) 70%);
  }

  .treatments-tab { left: 30px; top: 633px; width: 275px; height: 38px; }
  .treatments-heading {
    left: 62px; top: 642px;
    color: var(--white); font-size: 16px; font-weight: 700;
  }
  .treatments {
    left: 46px; top: 680px; list-style: none;
    font-size: 11.6px; font-weight: 300;
  }
  .treatments li { line-height: 18px; margin-bottom: 5px; padding-left: 10px; position: relative; }
  .treatments li::before { content: "▸"; position: absolute; left: 0; font-size: 7px; color: var(--olive); top: 0; }

  .approach {
    left: 360px; top: 655px; width: 396px;
    font-size: 13.6px; font-style: italic; font-weight: 300;
    line-height: 21.5px; text-align: right;
  }

  .clinician-photo {
    left: 384px; top: 752px; width: 78px; height: 78px; border-radius: 50%;
    border: 3px solid var(--white);
    background: linear-gradient(160deg, #8a4a34 0%, #d9b39d 50%, #b52a2a 100%);
  }
  .clinician-name { left: 474px; top: 753px; font-size: 13.5px; font-weight: 700; color: var(--forest); }
  .clinician-role { left: 474px; top: 773px; font-size: 11px; font-style: italic; font-weight: 300; }
  .license { top: 799px; font-size: 11px; font-weight: 300; line-height: 16px; }
  .license-nj { left: 474px; }
  .license-pa { left: 614px; }
  .license-divider { left: 602px; top: 800px; width: 1px; height: 32px; background: #9a9a7a; }

  .brand-name {
    left: 0; top: 884px; width: 780px; text-align: center;
    font-family: "Cinzel", "Times New Roman", serif;
    font-size: 31px; font-weight: 700; color: var(--forest); letter-spacing: 1px;
  }

  .phone-icon { left: 50px; top: 1011px; width: 48px; height: 48px; }
  .call-label {
    left: 109px; top: 1011px;
    font-family: "Cinzel", "Times New Roman", serif;
    font-size: 17px; color: var(--sand); letter-spacing: 0.5px;
  }
  .call-label::after { content: ""; display: inline-block; width: 30px; height: 1px; background: var(--sand); margin-left: 6px; vertical-align: 5px; }
  .call-number { left: 109px; top: 1033px; font-size: 25px; font-weight: 700; color: var(--white); }

  .web-bar {
    left: 430px; top: 1017px; width: 350px; height: 44px;
    background: var(--olive); border-left: 4px solid var(--sand);
    color: var(--white); font-size: 13.5px; font-weight: 700;
    line-height: 44px; padding-left: 24px;
  }
</style>
</head>
<body>
<main class="flyer">
  <div class="abs hero-photo" role="img" aria-label="Photo of a therapist with a notepad talking with a client on leather chairs"></div>

  <svg class="abs backdrop" viewBox="0 0 780 1094" aria-hidden="true">
    <path d="M0 375 C 180 340, 420 350, 780 430 L780 1094 L0 1094 Z" fill="var(--sand)"/>
    <path d="M0 620 C 200 600, 420 600, 560 610 L780 590 L780 1094 L0 1094 Z" fill="var(--sand-light)" opacity="0.5"/>
    <path d="M360 655 L780 655 L780 732 L334 732 Z" fill="var(--sand-light)"/>
    <rect x="0" y="923" width="780" height="8" fill="var(--olive)"/>
    <rect x="0" y="931" width="780" height="163" fill="var(--forest)"/>
  </svg>

  <h1 class="abs title">
    <span class="title-main">The Bridgewell</span>
    <span class="title-main">Counseling Group</span>
    <span class="title-sub">of Greater Philadelphia</span>
  </h1>
  <div class="abs title-rule"></div>

  <p class="abs intro">BCG provides expert clinical care for <strong>anxiety disorders, obsessive compulsive and related disorders</strong> and <strong>neurodevelopmental disorders</strong> in children, adolescents and adults.</p>

  <div class="abs circle-photo" role="img" aria-label="Photo of a distressed client holding her head while the therapist takes notes"></div>

  <p class="abs lead">BCG proudly provides the Greater Philadelphia community with state-of-the-art assessment and evidence-based therapy for disorders including:</p>

  <ul class="abs conditions conditions-left">
    <li>Obsessive Compulsive Disorder</li>
    <li>Trichotillomania Excoriation Disorder</li>
    <li>Generalized Anxiety Disorder</li>
    <li>Panic Disorder</li>
    <li>Specific Phobias</li>
    <li>Hoarding Disorder</li>
  </ul>
  <ul class="abs conditions conditions-right">
    <li>Body Dysmophic Disorder</li>
    <li>Tic Disorder</li>
    <li>ADHD Learning Disorder</li>
    <li>Insomnia</li>
    <li>Social Anxiety Disorder</li>
  </ul>

  <div class="abs head-illustration" role="img" aria-label="Illustration of a head in profile with colourful puzzle pieces in the brain"></div>

  <svg class="abs treatments-tab" viewBox="0 0 275 38" aria-hidden="true">
    <path d="M16 0 H275 L262 30 Q258 38 248 38 H0 L10 8 Q13 0 16 0 Z" fill="var(--forest)"/>
  </svg>
  <h2 class="abs treatments-heading">Treatments We Provide:</h2>
  <ul class="abs treatments">
    <li>Cognitive Behavioral Therapy (CBT)</li>
    <li>Exposure and Response Prevention (E/RP)</li>
    <li>Comprehensive Behavioral (ComB)/ Habit<br>Reversal Training (HRT)</li>
    <li>Cognitive Behavioral Intervention for Ties (CBIT)</li>
    <li>Acceptance and Commitment Therapy (ACT)</li>
    <li>Organizational Skills Training (OST)</li>
    <li>CBT for Insomnia (CBT-I)</li>
  </ul>

  <p class="abs approach">BCG clinicians are highly trained in cognitive behavioral therapy (CBT), which includes scientifically informed techniques that are tailored to each client’s unique needs.</p>

  <div class="abs clinician-photo" role="img" aria-label="Portrait photo of the executive director"></div>
  <p class="abs clinician-name">Dana R. Whitcombe PsyD</p>
  <p class="abs clinician-role">Executive Director Licensed Clinical Psychologist</p>
  <p class="abs license license-nj">New Jersey<br>Lic. No. 35S00000000</p>
  <div class="abs license-divider"></div>
  <p class="abs license license-pa">Pennsylvania<br>Lic. No. PS0000000</p>

  <p class="abs brand-name">The Bridgewell Counseling Group</p>

  <svg class="abs phone-icon" viewBox="0 0 48 48" aria-hidden="true">
    <circle cx="24" cy="24" r="24" fill="var(--olive)"/>
    <path d="M17 13 l4 -1 l3 7 l-3 2 q2 5 6 7 l2 -3 l7 3 l-1 4 q-1 3 -5 2 q-11 -3 -15 -15 q-1 -4 2 -6 Z" fill="var(--white)"/>
  </svg>
  <p class="abs call-label">Call Us Now</p>
  <p class="abs call-number">(555) 014-2387</p>

  <p class="abs web-bar">www.BridgewellCounselingGroup.com</p>
</main>
</body>
</html>
```